Unusual Options Activity Graphic Card Design for Finance App

We are developing a financial data platform called Vanta Pulse, and we need a visually striking, mobile-optimized graphic card design to display unusual options activity. The card will be featured in our mobile app and marketing materials, inspired by platforms like Grivox and Marlin Tide.
🔹 Design Goals:
Modern, clean, and professional aesthetic
Use vibrant electric blue, green, or dark theme gradients
Must feel tech-savvy and finance-oriented
Layout should be optimized for vertical mobile format (portrait)
🔹 Information to Include in the Card:
Ticker Symbol (e.g., QMZ) with colored badge
Date & Time of trade
Trade Type (e.g., Sweep Call / Put)
Execution Type (At Ask or At Bid)
Strike Price
Expiration Date
Premium (e.g., $342.75K)
Size@Price (e.g., 6995@$0.49)
Volume
Open Interest
Branding at bottom: “Vanta Pulse” in modern font
🔹 Inspiration:
Grivox’s profit/loss cards
Clean fintech dashboards (Quillpath, Marlin Tide, Halvorsen Console)
Please provide the final deliverable in high-resolution PNG and layered PSD or Figma file for future edits.
Stock Market Traders
Finance

```html
<!DOCTYPE html>
<html lang="en">
<head>
<meta charset="utf-8">
<title>Unusual Options Activity – Graphic Card Design</title>
<link href="https://fonts.googleapis.com/css2?family=Inter:wght@400;500;600;700;800&family=Plus+Jakarta+Sans:wght@700;800&display=swap" rel="stylesheet">
<style>
  :root{
    --page:#000;
    --ink:#ffffff;
    --muted:#a9b3cf;
    --card-top:#1b2444;
    --card-mid:#152a66;
    --card-bottom:#10307e;
    --call:#4ade80;
    --put:#ef4444;
    --badge-green:#3dd66b;
    --badge-red:#e0443e;
    --brand:#4fd46a;
    --blue-top:#3a5ee8;
    --blue-bottom:#1456d8;
    --panel:#1c1c1c;
    --bar:#3b3b3b;
  }
  *{box-sizing:border-box;margin:0;padding:0}
  html,body{width:1200px;height:975px;overflow:hidden;background:var(--page)}
  body{position:relative;font-family:"Inter",sans-serif;color:var(--ink)}
  .abs{position:absolute}

  /* heading */
  .board-title{position:absolute;left:49px;top:33px;width:300px;text-align:center;
    font-family:"Plus Jakarta Sans",sans-serif;font-weight:800;font-size:20px;line-height:24.5px;letter-spacing:-.2px}

  /* annotations */
  .callout{position:absolute;font-family:"Plus Jakarta Sans",sans-serif;font-weight:800;font-size:13.5px;line-height:16px;white-space:nowrap}
  .callout.left{right:1022px;transform:translateY(-50%)}
  .callout.right{transform:translateY(-50%)}
  .callout-lines{position:absolute;left:0;top:0;width:1200px;height:975px;pointer-events:none}

  .section-label{position:absolute;font-family:"Plus Jakarta Sans",sans-serif;font-weight:800;font-size:17px;transform:translateX(-50%)}

  /* option activity card */
  .uoa-card{position:absolute;width:129px;height:204px;border-radius:5px;overflow:hidden;
    background:linear-gradient(180deg,var(--card-top) 0%,var(--card-mid) 60%,var(--card-bottom) 100%);color:var(--ink)}
  .ticker-badge{position:absolute;left:10.5px;top:8px;width:19px;height:19px;border-radius:50%;
    background:var(--badge-green);font-size:5.6px;font-weight:700;display:flex;align-items:center;justify-content:center;color:#fff}
  .ticker-badge.bear{background:var(--badge-red)}
  .card-title{position:absolute;left:35px;top:6.5px;font-size:8.2px;font-weight:700;line-height:9.6px;text-transform:uppercase;letter-spacing:.1px}
  .trade-time{position:absolute;left:10.5px;top:34px;font-size:4.9px;color:#d5dbef}
  .trade-type{position:absolute;left:10.5px;top:49px;font-size:17.3px;font-weight:800;line-height:20px;letter-spacing:.2px;white-space:nowrap}
  .trade-type .call{color:var(--call)}
  .trade-type .put{color:var(--put)}
  .execution{position:absolute;left:10.5px;top:71px;font-size:6.4px;color:#9aa6c8}
  .sentiment{position:absolute;left:10.5px;top:80px;width:108px;height:36px;overflow:visible}
  .stats{position:absolute;left:10.5px;right:10.5px;top:118px;font-size:6.5px;line-height:9.2px}
  .stats div{display:flex;justify-content:space-between}
  .stats dt{color:var(--muted)}
  .stats dd{color:var(--ink)}
  .card-rule{position:absolute;left:10.5px;right:10.5px;top:179px;height:.6px;background:rgba(255,255,255,.25)}
  .brand{position:absolute;left:0;right:0;top:184px;display:flex;align-items:center;justify-content:center;gap:3px;
    font-size:7.2px;font-weight:800;color:var(--brand);letter-spacing:.2px;text-transform:uppercase}
  .brand-dot{width:8px;height:8px;border-radius:50%;background:var(--brand)}

  .uoa-card.electric{background:linear-gradient(165deg,var(--blue-top) 0%,#2272ee 50%,var(--blue-bottom) 100%)}
  .uoa-card.electric .stats dt{color:#d6e4ff}
  .uoa-card.electric .execution{color:#d6e4ff}
  .uoa-card.electric .card-rule{background:rgba(255,255,255,.4)}

  .uoa-card.light{background:#fff;color:#111}
  .uoa-card.light .stats dt{color:#444}
  .uoa-card.light .stats dd{color:#111}
  .uoa-card.light .trade-time{color:#333}
  .uoa-card.light .execution{color:#333}
  .uoa-card.light .card-rule{background:rgba(0,0,0,.2)}
  .uoa-card.light .brand{color:#1a1a1a}
  .uoa-card.light .brand-dot{background:var(--badge-green)}

  /* mobile app screen */
  .app-screen{position:absolute;left:101px;top:584px;width:163px;height:360px;overflow:hidden;background:#000}
  .status{position:absolute;left:0;right:0;top:8px;height:12px;font-size:6.8px;font-weight:600}
  .status .clock{position:absolute;left:20px;top:0}
  .status .icons{position:absolute;right:16px;top:2px}
  .app-heading{position:absolute;left:0;right:0;top:26px;text-align:center;font-size:7.6px}
  .tabs{position:absolute;left:0;right:0;top:42px;height:14px;border-bottom:.6px solid #333;font-size:5.4px}
  .tabs span{position:absolute;top:0;transform:translateX(-50%);white-space:nowrap}
  .tabs .active{color:var(--call)}
  .tabs .active::after{content:"";position:absolute;left:-2px;right:-2px;top:10px;height:1px;background:var(--call)}
  .tab-bar{position:absolute;left:0;right:0;top:322px;height:38px;background:#000}
  .tab-bar svg{position:absolute}
  .tab-bar .label{position:absolute;top:16px;font-size:4.6px;color:var(--call);transform:translateX(-50%)}
  .home-indicator{position:absolute;height:2px;border-radius:1px;background:#fff}

  /* web app screen */
  .web-screen{position:absolute;left:290px;top:583px;width:166px;height:358px;overflow:hidden;background:#000;border-radius:8px 8px 8px 8px}
  .web-status{position:absolute;left:0;right:0;top:0;height:24px;background:#fff;color:#000}
  .web-header{position:absolute;left:0;right:0;top:24px;height:35px;background:#1e1e1e}
  .web-header .brand-lockup{position:absolute;left:3px;top:15px;display:flex;align-items:center;gap:1.5px;font-size:4px;font-weight:800;color:var(--brand);text-transform:uppercase}
  .web-header .brand-lockup i{width:4px;height:4px;border-radius:50%;background:var(--brand)}
  .web-header .page-name{position:absolute;left:34px;top:14px;font-size:6px;font-weight:600}
  .toggle{position:absolute;border-radius:99px;background:#fff}
  .toggle::after{content:"";position:absolute;border-radius:50%;background:#111}
  .theme-toggle{left:91px;top:12px;width:22px;height:10px}
  .theme-toggle::after{left:1.5px;top:1.5px;width:7px;height:7px}
  .theme-toggle .moon{position:absolute;right:3px;top:2.5px;width:5px;height:5px;border-radius:50%;background:#f5c518}
  .avatar{position:absolute;left:123px;top:11px;width:12px;height:12px;border-radius:50%;background:linear-gradient(135deg,#c9ccd4,#6f7480)}
  .web-panel{position:absolute;left:0;right:0;top:59px;height:78px;background:var(--panel)}
  .web-panel .panel-title{position:absolute;left:4px;top:7px;font-size:7.3px;font-weight:500}
  .refresh-toggle{left:6px;top:26px;width:11px;height:5.5px}
  .refresh-toggle::after{left:1px;top:1px;width:3.5px;height:3.5px}
  .web-panel .refresh-label{position:absolute;left:22px;top:25px;font-size:5.3px}
  .search{position:absolute;left:5px;right:6px;top:44px;height:15px;border-radius:2px;background:#3a3a3a;font-size:5.3px;color:#9a9a9a;padding:4.5px 6px}
  .tools{position:absolute;left:12px;top:67px;font-size:5.3px;display:flex;align-items:center;gap:4px}
  .browser-bar{position:absolute;left:0;right:0;top:309px;height:49px;background:var(--bar)}
  .url-pill{position:absolute;left:13px;width:140px;top:3px;height:15px;border-radius:4px;background:#555;font-size:6px;text-align:center;line-height:15px}
  .browser-bar svg{position:absolute}

  /* closing */
  .thanks{position:absolute;left:985px;width:200px;top:873px;text-align:center}
  .thanks h2{font-family:"Plus Jakarta Sans",sans-serif;font-weight:800;font-size:31px;line-height:36px;letter-spacing:-.6px}
  .thanks p{font-size:11.2px;line-height:13px;margin-top:9px}
</style>
</head>
<body>

<svg width="0" height="0" style="position:absolute" aria-hidden="true">
  <defs>
    <linearGradient id="fill-call" x1="0" y1="0" x2="0" y2="1"><stop offset="0" stop-color="#4ade80" stop-opacity=".95"/><stop offset="1" stop-color="#4ade80" stop-opacity="0"/></linearGradient>
    <linearGradient id="fill-put" x1="0" y1="0" x2="0" y2="1"><stop offset="0" stop-color="#ef5a5a" stop-opacity=".95"/><stop offset="1" stop-color="#ef5a5a" stop-opacity="0"/></linearGradient>
    <linearGradient id="fill-flat" x1="0" y1="0" x2="0" y2="1"><stop offset="0" stop-color="#9aa3c0" stop-opacity=".6"/><stop offset="1" stop-color="#9aa3c0" stop-opacity="0"/></linearGradient>
    <g id="chart-rise">
      <polygon fill="url(#fill-call)" points="0,36 0,34 4,30 7,32 11,27 14,29 18,25 21,27 25,23 28,25 31,21 34,24 38,20 41,23 45,19 48,22 52,18 55,21 58,16 61,19 65,14 68,17 71,12 74,15 78,10 81,13 84,8 87,11 90,5 93,8 96,3 99,6 102,1 105,4 108,0 108,36"/>
      <polyline fill="none" stroke="#4ade80" stroke-width="1" points="0,34 4,30 7,32 11,27 14,29 18,25 21,27 25,23 28,25 31,21 34,24 38,20 41,23 45,19 48,22 52,18 55,21 58,16 61,19 65,14 68,17 71,12 74,15 78,10 81,13 84,8 87,11 90,5 93,8 96,3 99,6 102,1 105,4 108,0"/>
    </g>
    <g id="chart-rise-dark">
      <polygon fill="url(#fill-call)" points="0,36 0,34 4,30 7,32 11,27 14,29 18,25 21,27 25,23 28,25 31,21 34,24 38,20 41,23 45,19 48,22 52,18 55,21 58,16 61,19 65,14 68,17 71,12 74,15 78,10 81,13 84,8 87,11 90,5 93,8 96,3 99,6 102,1 105,4 108,0 108,36"/>
      <polyline fill="none" stroke="#1f2a44" stroke-width="1" points="0,34 4,30 7,32 11,27 14,29 18,25 21,27 25,23 28,25 31,21 34,24 38,20 41,23 45,19 48,22 52,18 55,21 58,16 61,19 65,14 68,17 71,12 74,15 78,10 81,13 84,8 87,11 90,5 93,8 96,3 99,6 102,1 105,4 108,0"/>
    </g>
    <g id="chart-fall" transform="translate(108,0) scale(-1,1)">
      <polygon fill="url(#fill-put)" points="0,36 0,34 4,30 7,32 11,27 14,29 18,25 21,27 25,23 28,25 31,21 34,24 38,20 41,23 45,19 48,22 52,18 55,21 58,16 61,19 65,14 68,17 71,12 74,15 78,10 81,13 84,8 87,11 90,5 93,8 96,3 99,6 102,1 105,4 108,0 108,36"/>
      <polyline fill="none" stroke="#ef5a5a" stroke-width="1" points="0,34 4,30 7,32 11,27 14,29 18,25 21,27 25,23 28,25 31,21 34,24 38,20 41,23 45,19 48,22 52,18 55,21 58,16 61,19 65,14 68,17 71,12 74,15 78,10 81,13 84,8 87,11 90,5 93,8 96,3 99,6 102,1 105,4 108,0"/>
    </g>
    <g id="chart-flat">
      <rect x="0" y="2" width="108" height="22" fill="url(#fill-flat)"/>
      <line x1="0" y1="2" x2="108" y2="2" stroke="#c4cadb" stroke-width="1"/>
    </g>
    <marker id="tip" viewBox="0 0 6 6" refX="5" refY="3" markerWidth="4" markerHeight="4" orient="auto"><path d="M0,0 L6,3 L0,6 Z" fill="#fff"/></marker>
  </defs>
</svg>

<h1 class="board-title">Unusual Options Activity :<br>Graphic Card Design for<br>Finance App</h1>

<!-- anatomy callouts -->
<span class="callout left" style="top:237px">Ticker Symbol</span>
<span class="callout left" style="top:271px">Trade Type</span>
<span class="callout left" style="top:297px">Execution Type</span>
<span class="callout left" style="top:334px">Sentiment</span>
<span class="callout left" style="top:407px">Branding</span>
<span class="callout right" style="left:385px;top:249px">Date &amp; Time of trade</span>
<span class="callout right" style="left:409px;top:277px">C/P</span>

<svg class="callout-lines" viewBox="0 0 1200 975" aria-hidden="true">
  <g fill="none" stroke="#fff" stroke-width=".9" marker-end="url(#tip)">
    <path d="M185,240 C195,225 215,222 231,234"/>
    <path d="M185,276 C195,262 215,261 231,275"/>
    <path d="M185,297 C195,283 215,282 231,296"/>
    <path d="M185,331 C195,317 215,316 231,328"/>
    <path d="M185,407 C195,393 215,392 231,407"/>
    <path d="M381,249 C340,240 300,243 281,257"/>
    <path d="M402,276 C385,262 360,266 345,276"/>
  </g>
  <g fill="#fff">
    <circle cx="185" cy="240" r="1.6"/><circle cx="185" cy="276" r="1.6"/><circle cx="185" cy="297" r="1.6"/>
    <circle cx="185" cy="331" r="1.6"/><circle cx="185" cy="407" r="1.6"/><circle cx="381" cy="249" r="1.6"/><circle cx="402" cy="276" r="1.6"/>
  </g>
</svg>

<!-- anatomy card -->
<article class="uoa-card" style="left:225px;top:218px">
  <span class="ticker-badge">GVR</span>
  <h3 class="card-title">Unusual Options<br>Activity</h3>
  <time class="trade-time">17 Apr 25, 10:32</time>
  <p class="trade-type">TRADE <span class="call">CALL</span></p>
  <p class="execution">AT ASk</p>
  <svg class="sentiment" viewBox="0 0 108 36"><use href="#chart-rise"/></svg>
  <dl class="stats"><div><dt>Strike</dt><dd>$91</dd></div><div><dt>Expiration</dt><dd>19 Apr 25</dd></div><div><dt>Premium</dt><dd>$342.75K</dd></div><div><dt>Size@Price</dt><dd>6995@$0.49</dd></div><div><dt>Volume</dt><dd>34.7K</dd></div><div><dt>Open Interest</dt><dd>2424</dd></div></dl>
  <span class="card-rule"></span>
  <footer class="brand"><i class="brand-dot"></i>Vanta Pulse</footer>
</article>

<!-- variant grid -->
<article class="uoa-card" style="left:636px;top:92px">
  <span class="ticker-badge">QMZ</span>
  <h3 class="card-title">Unusual Options<br>Activity</h3>
  <time class="trade-time">04 Apr 25, 16:14:59</time>
  <p class="trade-type">SWEEP <span class="call">CALL</span></p>
  <p class="execution">AT BID</p>
  <svg class="sentiment" viewBox="0 0 108 36"><use href="#chart-fall"/></svg>
  <dl class="stats"><div><dt>Strike</dt><dd>$88</dd></div><div><dt>Expiration</dt><dd>25 Apr 25</dd></div><div><dt>Premium</dt><dd>$343K</dd></div><div><dt>Size@Price</dt><dd>6995@$0.49</dd></div><div><dt>Volume</dt><dd>15804</dd></div><div><dt>Open Interest</dt><dd>2424</dd></div></dl>
  <span class="card-rule"></span>
  <footer class="brand"><i class="brand-dot"></i>Vanta Pulse</footer>
</article>

<article class="uoa-card" style="left:776px;top:92px">
  <span class="ticker-badge">GVR</span>
  <h3 class="card-title">Unusual Options<br>Activity</h3>
  <time class="trade-time">17 Apr 25, 10:32</time>
  <p class="trade-type">TRADE <span class="call">CALL</span></p>
  <p class="execution">AT ASk</p>
  <svg class="sentiment" viewBox="0 0 108 36"><use href="#chart-rise"/></svg>
  <dl class="stats"><div><dt>Strike</dt><dd>$91</dd></div><div><dt>Expiration</dt><dd>19 Apr 25</dd></div><div><dt>Premium</dt><dd>$342.75K</dd></div><div><dt>Size@Price</dt><dd>6995@$0.49</dd></div><div><dt>Volume</dt><dd>34.7K</dd></div><div><dt>Open Interest</dt><dd>2424</dd></div></dl>
  <span class="card-rule"></span>
  <footer class="brand"><i class="brand-dot"></i>Vanta Pulse</footer>
</article>

<article class="uoa-card" style="left:916px;top:92px">
  <span class="ticker-badge">GVR</span>
  <h3 class="card-title">Unusual Options<br>Activity</h3>
  <time class="trade-time">17 Apr 25, 10:32</time>
  <p class="trade-type">SWEEP <span class="call">CALL</span></p>
  <p class="execution">AT ASk</p>
  <svg class="sentiment" viewBox="0 0 108 36"><use href="#chart-flat"/></svg>
  <dl class="stats"><div><dt>Strike</dt><dd>$91</dd></div><div><dt>Expiration</dt><dd>19 Apr 25</dd></div><div><dt>Premium</dt><dd>$342.75K</dd></div><div><dt>Size@Price</dt><dd>6995@$0.49</dd></div><div><dt>Volume</dt><dd>34.7K</dd></div><div><dt>Open Interest</dt><dd>2424</dd></div></dl>
  <span class="card-rule"></span>
  <footer class="brand"><i class="brand-dot"></i>Vanta Pulse</footer>
</article>

<article class="uoa-card" style="left:636px;top:307px">
  <span class="ticker-badge bear">QMZ</span>
  <h3 class="card-title">Unusual Options<br>Activity</h3>
  <time class="trade-time">17 Apr 25, 10:32</time>
  <p class="trade-type">SWEEP <span class="put">PUT</span></p>
  <p class="execution">AT BID</p>
  <svg class="sentiment" viewBox="0 0 108 36"><use href="#chart-fall"/></svg>
  <dl class="stats"><div><dt>Strike</dt><dd>$91</dd></div><div><dt>Expiration</dt><dd>19 Apr 25</dd></div><div><dt>Premium</dt><dd>$343K</dd></div><div><dt>Size@Price</dt><dd>6995@$0.49</dd></div><div><dt>Volume</dt><dd>34.7K</dd></div><div><dt>Open Interest</dt><dd>2424</dd></div></dl>
  <span class="card-rule"></span>
  <footer class="brand"><i class="brand-dot"></i>Vanta Pulse</footer>
</article>

<article class="uoa-card" style="left:776px;top:307px">
  <span class="ticker-badge bear">QMZ</span>
  <h3 class="card-title">Unusual Options<br>Activity</h3>
  <time class="trade-time">17 Apr 25, 10:32</time>
  <p class="trade-type">TRADE <span class="put">PUT</span></p>
  <p class="execution">AT BID</p>
  <svg class="sentiment" viewBox="0 0 108 36"><use href="#chart-rise"/></svg>
  <dl class="stats"><div><dt>Strike</dt><dd>$91</dd></div><div><dt>Expiration</dt><dd>19 Apr 25</dd></div><div><dt>Premium</dt><dd>$342.75K</dd></div><div><dt>Size@Price</dt><dd>6995@$0.49</dd></div><div><dt>Volume</dt><dd>34.7K</dd></div><div><dt>Open Interest</dt><dd>2424</dd></div></dl>
  <span class="card-rule"></span>
  <footer class="brand"><i class="brand-dot"></i>Vanta Pulse</footer>
</article>

<article class="uoa-card" style="left:916px;top:307px">
  <span class="ticker-badge bear">QMZ</span>
  <h3 class="card-title">Unusual Options<br>Activity</h3>
  <time class="trade-time">17 Apr 25, 10:32</time>
  <p class="trade-type">TRADE <span class="put">PUT</span></p>
  <p class="execution">AT BID</p>
  <svg class="sentiment" viewBox="0 0 108 36"><use href="#chart-flat"/></svg>
  <dl class="stats"><div><dt>Strike</dt><dd>$91</dd></div><div><dt>Expiration</dt><dd>19 Apr 25</dd></div><div><dt>Premium</dt><dd>$342.75K</dd></div><div><dt>Size@Price</dt><dd>6995@$0.49</dd></div><div><dt>Volume</dt><dd>34.7K</dd></div><div><dt>Open Interest</dt><dd>2424</dd></div></dl>
  <span class="card-rule"></span>
  <footer class="brand"><i class="brand-dot"></i>Vanta Pulse</footer>
</article>

<!-- colour themes -->
<article class="uoa-card electric" style="left:647px;top:619px">
  <span class="ticker-badge">QMZ</span>
  <h3 class="card-title">Unusual Options<br>Activity</h3>
  <time class="trade-time">17 Apr 25, 10:32</time>
  <p class="trade-type">SWEEP <span class="call">CALL</span></p>
  <p class="execution">AT ASk</p>
  <svg class="sentiment" viewBox="0 0 108 36"><use href="#chart-rise"/></svg>
  <dl class="stats"><div><dt>Strike</dt><dd>$91</dd></div><div><dt>Expiration</dt><dd>19 Apr 25</dd></div><div><dt>Premium</dt><dd>$342.75K</dd></div><div><dt>Size@Price</dt><dd>6995@$0.49</dd></div><div><dt>Volume</dt><dd>34.7K</dd></div><div><dt>Open Interest</dt><dd>2424</dd></div></dl>
  <span class="card-rule"></span>
  <footer class="brand"><i class="brand-dot"></i>Vanta Pulse</footer>
</article>

<article class="uoa-card light" style="left:798px;top:619px">
  <span class="ticker-badge">QMZ</span>
  <h3 class="card-title">Unusual Options<br>Activity</h3>
  <time class="trade-time">17 Apr 25, 10:32</time>
  <p class="trade-type">SWEEP <span class="call">CALL</span></p>
  <p class="execution">AT ASk</p>
  <svg class="sentiment" viewBox="0 0 108 36"><use href="#chart-rise-dark"/></svg>
  <dl class="stats"><div><dt>Strike</dt><dd>$91</dd></div><div><dt>Expiration</dt><dd>19 Apr 25</dd></div><div><dt>Premium</dt><dd>$342.75K</dd></div><div><dt>Size@Price</dt><dd>6995@$0.49</dd></div><div><dt>Volume</dt><dd>34.7K</dd></div><div><dt>Open Interest</dt><dd>2424</dd></div></dl>
  <span class="card-rule"></span>
  <footer class="brand"><i class="brand-dot"></i>Vanta Pulse</footer>
</article>

<!-- app mockups -->
<span class="section-label" style="left:175px;top:545px">APP</span>
<span class="section-label" style="left:370px;top:541px">Web APP</span>

<section class="app-screen">
  <div class="status"><span class="clock">7:09</span>
    <svg class="icons" width="32" height="7" viewBox="0 0 32 7"><g fill="#fff"><rect x="0" y="4" width="1.5" height="3"/><rect x="2.3" y="3" width="1.5" height="4"/><rect x="4.6" y="1.5" width="1.5" height="5.5"/><rect x="6.9" y="0" width="1.5" height="7"/><path d="M11,2.5 Q15,-1 19,2.5 L18,3.5 Q15,1 12,3.5Z M13,4.5 Q15,3 17,4.5 L15,7Z"/><rect x="21" y="1" width="10" height="5" rx="1.3"/></g></svg>
  </div>
  <p class="app-heading">Markets</p>
  <nav class="tabs"><span class="active" style="left:20px">Option Flow</span><span style="left:59px">Darkpool</span><span style="left:94px">Treemap</span><span style="left:126.5px">Gamma</span><span style="left:155.5px">Snaps</span></nav>

  <article class="uoa-card" style="left:17px;top:71px">
    <span class="ticker-badge">QMZ</span>
    <h3 class="card-title">Unusual Options<br>Activity</h3>
    <time class="trade-time">17 Apr 25, 10:32</time>
    <p class="trade-type">SWEEP <span class="call">CALL</span></p>
    <p class="execution">AT ASk</p>
    <svg class="sentiment" viewBox="0 0 108 36"><use href="#chart-rise"/></svg>
    <dl class="stats"><div><dt>Strike</dt><dd>$91</dd></div><div><dt>Expiration</dt><dd>19 Apr 25</dd></div><div><dt>Premium</dt><dd>$342.75K</dd></div><div><dt>Size@Price</dt><dd>6995@$0.49</dd></div><div><dt>Volume</dt><dd>34.7K</dd></div><div><dt>Open Interest</dt><dd>2424</dd></div></dl>
    <span class="card-rule"></span>
    <footer class="brand"><i class="brand-dot"></i>Vanta Pulse</footer>
  </article>
  <article class="uoa-card" style="left:17px;top:289px">
    <span class="ticker-badge">QMZ</span>
    <h3 class="card-title">Unusual Options<br>Activity</h3>
  </article>

  <nav class="tab-bar">
    <svg style="left:10px;top:8px" width="7" height="7" viewBox="0 0 7 7"><g fill="#bbb"><rect width="3" height="3"/><rect x="4" width="3" height="3"/><rect y="4" width="3" height="3"/><rect x="4" y="4" width="3" height="3"/></g></svg>
    <svg style="left:41px;top:7px" width="6" height="8" viewBox="0 0 6 8"><rect width="6" height="8" rx="1" fill="#bbb"/><g stroke="#000" stroke-width=".7"><line x1="1.3" y1="3" x2="4.7" y2="3"/><line x1="1.3" y1="5" x2="4.7" y2="5"/></g></svg>
    <svg style="left:77px;top:5px" width="9" height="6" viewBox="0 0 9 6"><polyline points="0,5 3,2.5 5,4 9,0" fill="none" stroke="#4ade80" stroke-width="1"/></svg>
    <span class="label" style="left:81.5px">Markets</span>
    <svg style="left:115px;top:7px" width="7" height="7" viewBox="0 0 7 7"><g fill="#bbb"><rect x="0" y="3" width="1.8" height="4"/><rect x="2.6" y="0" width="1.8" height="7"/><rect x="5.2" y="2" width="1.8" height="5"/></g></svg>
    <svg style="left:146px;top:7px" width="6" height="7" viewBox="0 0 6 7"><g fill="#bbb"><circle cx="3" cy="2" r="1.8"/><path d="M0,7 Q3,2.5 6,7Z"/></g></svg>
  </nav>
  <span class="home-indicator" style="left:52px;width:59px;top:352px"></span>
</section>

<section class="web-screen">
  <div class="web-status">
    <span class="abs" style="left:20px;top:8px;font-size:6.8px;font-weight:600">7:09</span>
    <svg class="abs" style="right:15px;top:10px" width="32" height="7" viewBox="0 0 32 7"><g fill="#000"><rect x="0" y="4" width="1.5" height="3"/><rect x="2.3" y="3" width="1.5" height="4"/><rect x="4.6" y="1.5" width="1.5" height="5.5"/><rect x="6.9" y="0" width="1.5" height="7"/><path d="M11,2.5 Q15,-1 19,2.5 L18,3.5 Q15,1 12,3.5Z M13,4.5 Q15,3 17,4.5 L15,7Z"/><rect x="21" y="1" width="10" height="5" rx="1.3"/></g></svg>
  </div>
  <header class="web-header">
    <span class="brand-lockup"><i></i>Vanta Pulse</span>
    <span class="page-name">Option Flow</span>
    <span class="toggle theme-toggle"><span class="moon"></span></span>
    <span class="avatar" role="img" aria-label="User profile photo"></span>
    <svg class="abs" style="left:139px;top:15.5px" width="5" height="3" viewBox="0 0 5 3"><polyline points="0,0 2.5,2.5 5,0" fill="none" stroke="#ccc" stroke-width=".7"/></svg>
    <svg class="abs" style="left:152px;top:14px" width="7" height="6" viewBox="0 0 7 6"><g stroke="#ddd" stroke-width=".8"><line x1="0" y1="1" x2="7" y2="1"/><line x1="0" y1="3" x2="7" y2="3"/><line x1="0" y1="5" x2="7" y2="5"/></g></svg>
  </header>
  <div class="web-panel">
    <p class="panel-title">Option Flow Data</p>
    <span class="toggle refresh-toggle"></span>
    <span class="refresh-label">Auto Refresh</span>
    <div class="search">Search Ticker...</div>
    <div class="tools">
      <svg width="8" height="5" viewBox="0 0 8 5"><g stroke="#fff" stroke-width=".7"><line x1="0" y1=".5" x2="8" y2=".5"/><line x1="1.5" y1="2.5" x2="6.5" y2="2.5"/><line x1="3" y1="4.5" x2="5" y2="4.5"/></g></svg>
      <span>Filter</span>
      <svg style="margin-left:4px" width="6" height="8" viewBox="0 0 6 8"><g fill="none" stroke="#fff" stroke-width=".7"><path d="M1.5,3 H0.5 V7.5 H5.5 V3 H4.5"/><line x1="3" y1="0.5" x2="3" y2="5"/><polyline points="1.5,2 3,0.5 4.5,2"/></g></svg>
      <span>Export</span>
    </div>
  </div>

  <article class="uoa-card" style="left:18px;top:156px">
    <span class="ticker-badge">QMZ</span>
    <h3 class="card-title">Unusual Options<br>Activity</h3>
    <time class="trade-time">17 Apr 25, 10:32</time>
    <p class="trade-type">SWEEP <span class="call">CALL</span></p>
    <p class="execution">AT ASk</p>
    <svg class="sentiment" viewBox="0 0 108 36"><use href="#chart-rise"/></svg>
    <dl class="stats"><div><dt>Strike</dt><dd>$91</dd></div><div><dt>Expiration</dt><dd>19 Apr 25</dd></div><div><dt>Premium</dt><dd>$342.75K</dd></div><div><dt>Size@Price</dt><dd>6995@$0.49</dd></div></dl>
  </article>

  <div class="browser-bar">
    <div class="url-pill">&#128274; app.vantapulse.com</div>
    <svg style="left:21px;top:7px" width="6" height="6" viewBox="0 0 6 6"><rect x=".4" y=".4" width="5.2" height="4" fill="none" stroke="#ddd" stroke-width=".7"/><line x1="1" y1="5.6" x2="5" y2="5.6" stroke="#ddd" stroke-width=".7"/></svg>
    <svg style="left:142px;top:7px" width="6" height="6" viewBox="0 0 6 6"><path d="M5,3 A2,2 0 1 1 4,1.2" fill="none" stroke="#ddd" stroke-width=".7"/><polyline points="3.5,0 4.3,1.3 3,1.8" fill="none" stroke="#ddd" stroke-width=".7"/></svg>
    <g></g>
    <svg style="left:0;top:22px" width="166" height="14" viewBox="0 0 166 14">
      <g fill="none" stroke="#4a8cf0" stroke-width=".9">
        <polyline points="12,4 9,7 12,10"/>
        <polyline points="46,4 49,7 46,10" stroke="#777"/>
        <path d="M80,6 H79 V12 H87 V6 H86 M83,2 V9 M81,4 L83,2 L85,4"/>
        <path d="M113,4 Q116,3 118,5 Q120,3 123,4 V11 Q120,10 118,12 Q116,10 113,11Z M118,5 V12"/>
        <rect x="148" y="5" width="6" height="6" rx="1"/><path d="M150,3 H156 V9"/>
      </g>
    </svg>
  </div>
  <span class="home-indicator" style="left:54px;width:58px;top:352px"></span>
</section>

<!-- closing -->
<div class="thanks">
  <h2>Thank you</h2>
  <p>Your feedback matters to us. Let us know what you think!</p>
</div>

</body>
</html>
```